CRM Banner Ad Design

Design banner ads to run in various ad networks.

We provide an online CRM (Customer Relationship Management) and Email Marketing solution for sales teams in Small and Medium sized businesses.

We'd like to include our logo in the ads for branding purposes and are flexible on the colors used as long as they don't clash with the logo.

Key messages are:

"CRM that comes loaded with leads"
or
"Does your CRM do email?"

Our target is sales organizations and the unique value proposition we offer is that our email marketing is bundled right into the CRM system the sales team uses and sales people can access 250 targeted business contacts each month.

Ad dimensions are 728 wide by 90 high (pixels)

Target Market(s)

Businesses with at least $10m in annual revenue and 10 sales people

Industry/Entity Type

Business

Requirements
Must have
• Ad dimensions are 728 wide by 90 high (pixels)

Call to action -

Either...
30 Day Free Trial with 250 Targeted Contacts
or
See how it works in this short video

exact verbiage can be flexible but, must have these general directions.
Should not have
• no offensive language or sexy images

```html
<!DOCTYPE html>
<html lang="en">
<head>
<meta charset="utf-8">
<title>CRM Banner Ad</title>
<link rel="stylesheet" href="https://fonts.googleapis.com/css2?family=Tinos&display=swap">
<style>
  :root {
    --paper: #ffffff;
    --ink: #000000;
    --accent: #e8531f;
  }
  html, body {
    margin: 0;
    padding: 0;
    overflow: hidden;
    background: var(--paper);
  }
  .banner {
    position: relative;
    width: 1200px;
    height: 148px;
    overflow: hidden;
    background: var(--paper);
    font-family: "Tinos", "Times New Roman", serif;
    color: var(--ink);
  }
  .headline,
  .offer,
  .cta {
    position: absolute;
    margin: 0;
    font-weight: 400;
    font-size: 48px;
    line-height: 1;
    white-space: nowrap;
  }
  .headline { left: 258px; top: -4px; }
  .offer    { left: 153px; top: 42px; }
  .cta      { left: 160px; top: 87px; }
  .brand {
    position: absolute;
    left: 820px;
    top: 98px;
    height: 44px;
    display: flex;
    align-items: center;
    gap: 12px;
  }
  .brand-mark {
    width: 22px;
    height: 22px;
    background: var(--accent);
  }
  .brand-name {
    font-size: 40px;
    font-weight: 400;
    line-height: 44px;
    color: var(--ink);
  }
</style>
</head>
<body>
  <div class="banner">
    <h1 class="headline">Does youur crm do email?</h1>
    <p class="offer">30 days freetrailwith250trageted Contacts</p>
    <p class="cta">join Now</p>
    <div class="brand">
      <span class="brand-mark" aria-hidden="true"></span>
      <span class="brand-name">dealorbit</span>
    </div>
  </div>
</body>
</html>
```